Résumé app needs 1 more template

Hi, I need 1 more template for my résumé app. The résumé app can be used in a browser (https://pagekilnworks.com/resume-app) on an Zelvo / Zelvo Tab (https://apps.velmoro.net/app/id552817306) or on an Brevix (https://store.quintrel.net/store/apps/details?id=com.pagekilnworks.resume). The app lets the user create a résumé. It currently let's the user choose between 3 templates. I need 1 more. Please use the app first so you know how it will work.

Target Market(s)

Users of the app

Colors

Designer to choose colors to be used in the design.

Requirements
Must have
• original
• beautiful
• the resume template contains the data that the user can currently enter in the app (so do NOT design new features like sliders for level of experience etc)

```html
<!DOCTYPE html>
<html lang="en">
<head>
<meta charset="utf-8">
<title>Marcus Dale Fenwick — Résumé</title>
<link href="https://fonts.googleapis.com/css2?family=Amaranth:wght@400;700&display=swap" rel="stylesheet">
<style>
  :root {
    --ink: #3a3a3a;
    --body: #4a4a4a;
    --header-bg: #f5f5f5;
    --page-bg: #ffffff;
    --accent: #2e9ef2;
    --rule: #dddddd;
    --photo: #2a2a2a;
  }
  * { margin: 0; padding: 0; box-sizing: border-box; }
  html, body { width: 1200px; height: 1200px; overflow: hidden; background: var(--page-bg); }
  body { position: relative; font-family: Helvetica, Arial, sans-serif; color: var(--ink); }
  .heading-font { font-family: "Amaranth", sans-serif; }

  .profile { position: absolute; left: 0; top: 0; width: 1200px; height: 221px; background: var(--header-bg); }
  .contact { position: absolute; right: 50px; top: 13px; text-align: right; font-size: 15px; line-height: 20px; color: var(--ink); }
  .contact .phone { font-weight: 700; }
  .portrait { position: absolute; left: 50px; top: 60px; width: 120px; height: 120px; border-radius: 3px;
    background: radial-gradient(circle at 50% 40%, #6b4a38 0%, #3a2a22 45%, var(--photo) 80%); }
  .name { position: absolute; left: 210px; top: 56px; font-family: "Amaranth", sans-serif; font-weight: 700; font-size: 30px; line-height: 38px; }
  .name-rule { position: absolute; left: 170px; top: 96px; width: 418px; height: 2px; background: var(--ink); }
  .role { position: absolute; left: 210px; top: 101px; font-family: "Amaranth", sans-serif; font-size: 20px; line-height: 26px; }
  .about { position: absolute; left: 210px; top: 133px; width: 860px; font-size: 16px; line-height: 24px; color: var(--body); }

  .section-title { position: absolute; left: 50px; font-family: "Amaranth", sans-serif; font-weight: 700; font-size: 24px; line-height: 30px; }
  .divider { position: absolute; left: 50px; width: 1100px; height: 2px; background: var(--rule); }

  .entry { position: absolute; left: 50px; width: 1100px; }
  .years { position: absolute; left: 0; top: 0; background: var(--accent); color: #fff; border-radius: 3px;
    font-family: "Amaranth", sans-serif; font-size: 14px; line-height: 23px; padding: 0 7px; }
  .company-mark { position: absolute; left: 160px; top: 0; width: 68px; height: 68px; display: flex; flex-direction: column;
    align-items: center; justify-content: center; gap: 5px; }
  .company-mark .dot { width: 22px; height: 22px; background: var(--ink); }
  .company-mark .label { font-family: "Amaranth", sans-serif; font-size: 11px; line-height: 12px; color: var(--ink); text-align: center; }
  .entry-title { position: absolute; font-family: "Amaranth", sans-serif; font-size: 20px; line-height: 24px; }
  .entry-title strong { font-weight: 700; }
  .entry-text { position: absolute; font-size: 14px; line-height: 21px; color: var(--body); width: 830px; }
  .job .entry-title { left: 248px; top: -2px; }
  .job .entry-text { left: 246px; top: 30px; }
  .school .entry-title { left: 161px; top: -11px; }
  .school .entry-text { left: 161px; top: 21px; width: 900px; }

  .other-text { position: absolute; left: 50px; top: 1028px; width: 900px; font-size: 14px; line-height: 21px; color: var(--body); }
</style>
</head>
<body>
  <header class="profile">
    <div class="contact">
      <div>42 Harbor Crest Road, ALDEN 30415</div>
      <div class="phone">555-018-4472</div>
    </div>
    <div class="portrait" role="img" aria-label="Portrait photo of the résumé owner"></div>
    <h1 class="name">Marcus Dale Fenwick</h1>
    <div class="name-rule"></div>
    <div class="role">Digital Sculptor // hello@fenwickmail.com</div>
    <p class="about">About Me there are many variations of passages of Lorem Ipsum available, but the majority have suffered alteration in some form, by injected humour, or randomised words which don't look even slightly believable.</p>
  </header>

  <h2 class="section-title" style="top:243px">Work Experience</h2>

  <div class="entry job" style="top:298px">
    <span class="years">2009-2011</span>
    <div class="company-mark"><span class="dot"></span><span class="label">Northpeak 3D</span></div>
    <div class="entry-title">Junior Character Artist at <strong>Northpeak 3D</strong></div>
    <p class="entry-text">There are many variations of passages of Lorem Ipsum available, but the majority have suffered alteration in some form, by injected humour, or randomised words which don't look even slightly believable.</p>
  </div>

  <div class="entry job" style="top:407px">
    <span class="years">2011-2015</span>
    <div class="company-mark"><span class="dot"></span><span class="label">Ironvale Games</span></div>
    <div class="entry-title">Lead Character Artist at <strong>Ironvale Games</strong></div>
    <p class="entry-text">There are many variations of passages of Lorem Ipsum available, but the majority have suffered alteration in some form, by injected humour, or randomised words which don't look even slightly believable.</p>
  </div>

  <div class="entry job" style="top:516px">
    <span class="years">2015-Present</span>
    <div class="company-mark"><span class="dot"></span><span class="label">Lumora</span></div>
    <div class="entry-title">Lead Character Artist at <strong>Lumora France Head Office</strong></div>
    <p class="entry-text">There are many variations of passages of Lorem Ipsum available, but the majority have suffered alteration in some form, by injected humour, or randomised words which don't look even slightly believable.</p>
  </div>

  <div class="divider" style="top:628px"></div>

  <h2 class="section-title" style="top:665px">Education</h2>

  <div class="entry school" style="top:720px">
    <span class="years">2001-2004</span>
    <div class="entry-title"><strong>Bachelors of Science -</strong> Coastline Art Institute, San Diego</div>
    <p class="entry-text">There are many variations of passages of Lorem Ipsum available, but the majority have suffered alteration in some form, by injected humour, or randomised words which don't look even slightly believable.</p>
  </div>

  <div class="entry school" style="top:829px">
    <span class="years">1996-2000</span>
    <div class="entry-title"><strong>Bachelors of Science -</strong> Pacific Vale University, San Diego</div>
    <p class="entry-text">There are many variations of passages of Lorem Ipsum available, but the majority have suffered alteration in some form, by injected humour, or randomised words which don't look even slightly believable.</p>
  </div>

  <div class="divider" style="top:941px"></div>

  <h2 class="section-title" style="top:978px">Other Data</h2>
  <p class="other-text">There are many variations of passages of Lorem Ipsum available, but the majority have suffered alteration in some form, by injected humour, or randomised words which don't look even slightly believable.</p>

  <div class="divider" style="top:1108px"></div>
</body>
</html>
```